Logo and Card design for KRV Home Solutions LLC

I need an edgier logo and business card designs. Current logo attached. I like the colors below. I would like the logo to incorporate a home in the design.
Title = Principal-Acquisitions
Email:KRVHOMESOLUTIONS@mailnest.example
555-014-2739
facebook
IG
2 sided business card with the front being contact info a slogan about selling a home fast. The back incorporating What we do. Buy houses, land, or commercial property as is. We find solutions to make the process of selling simple and fair.

Target Market(s)

Motivated house sellers.

Industry/Entity Type

Business

Contact Information for Business Card

Who we are: We are a Faith based Real Estate Investment Company. We pay cash for homes in any condition and can close quick. Whatever the reason you need to sell fast, we can help. We believe in creating win-win solutions to help you in your time of need. We care! We can help!

Logo Text

KRV Home Solutions LLC

Font styles to use
Sans Serif

Colors
33a6d7
0355a3
85abd2
cee9f5
9d9d9d
b2b2b2
ffffff

Requirements
Must have
• Old logo attached. I want something edgier.
• Company name, phone number, description on the back of what we can do. Pay all cash. Buy in as is condition. No fees,Commisions or closing costs.Close quick. No hassles with solutions to meet your unique situation.
• Call today for an offer within 24 hours.

```html
<!DOCTYPE html>
<html lang="en">
<head>
<meta charset="utf-8">
<title>KRV Home Solutions – Business Card</title>
<link href="https://fonts.googleapis.com/css2?family=Montserrat:wght@500;700&family=Bebas+Neue&family=Varela+Round&display=swap" rel="stylesheet">
<style>
  :root {
    --navy: #233a73;
    --navy-ink: #1e3676;
    --white: #ffffff;
    --grey-text: #4a4a4a;
    --grey-soft: #6b6b6b;
    --stage: #2b2b2b;
  }
  * { margin: 0; padding: 0; box-sizing: border-box; }
  html, body { width: 1200px; height: 852px; overflow: hidden; background: var(--stage); }
  .canvas { position: relative; width: 1200px; height: 852px; }

  .card {
    position: absolute;
    left: 260px;
    width: 680px;
    height: 388px;
    box-shadow: 0 10px 30px rgba(0,0,0,.45);
  }

  /* Back side */
  .card-back { top: 24px; background: var(--navy); color: var(--white); text-align: center; }
  .card-back .brand {
    position: absolute; top: 110px; left: 0; right: 0;
    display: flex; align-items: center; justify-content: center; gap: 12px;
  }
  .brand-mark { width: 22px; height: 22px; background: currentColor; flex: none; }
  .brand-name {
    font-family: "Montserrat", sans-serif; font-weight: 700;
    font-size: 34px; letter-spacing: 1px; text-transform: uppercase;
  }
  .offer {
    position: absolute; top: 210px; left: 90px; right: 90px;
    font-family: "Varela Round", sans-serif; font-size: 17px; line-height: 1.3;
    letter-spacing: .6px;
  }

  /* Front side */
  .card-front { top: 440px; background: var(--white); }
  .card-front .brand {
    position: absolute; top: 52px; left: 48px;
    display: flex; align-items: center; gap: 12px; color: var(--navy-ink);
  }
  .card-front .brand-name { font-size: 30px; }

  .contacts {
    position: absolute; top: 150px; left: 48px; list-style: none;
    font-family: "Varela Round", sans-serif; font-size: 19px;
    color: var(--grey-text); letter-spacing: .6px;
  }
  .contacts li { display: flex; align-items: center; gap: 10px; height: 28px; white-space: nowrap; }
  .contacts .icon { width: 18px; height: 18px; flex: none; }
  .contacts .dot { width: 16px; height: 16px; border-radius: 50%; background: var(--navy-ink); flex: none; margin: 0 1px; }

  .title-block {
    position: absolute; top: 146px; right: 54px; text-align: right;
  }
  .company {
    font-family: "Bebas Neue", sans-serif; font-size: 46px; line-height: 1;
    font-weight: 400; color: var(--navy-ink); letter-spacing: .5px; white-space: nowrap;
  }
  .role {
    font-family: "Varela Round", sans-serif; font-size: 19px;
    color: var(--grey-text); letter-spacing: 1px; line-height: 1.2;
  }
  .edge-bar {
    position: absolute; right: 0; top: 146px; width: 14px; height: 76px; background: var(--navy-ink);
  }

  .slogan {
    position: absolute; bottom: 34px; left: 0; right: 0; text-align: center;
    font-family: "Montserrat", sans-serif; font-weight: 500; font-size: 21px;
    letter-spacing: 5px; color: var(--grey-soft); text-transform: uppercase;
  }
</style>
</head>
<body>
<main class="canvas">

  <section class="card card-back" aria-label="Card back">
    <div class="brand">
      <span class="brand-mark" aria-hidden="true"></span>
      <span class="brand-name">KRV Home Solutions</span>
    </div>
    <p class="offer">
      Pay all cash. Buy in as is condition. No fees,Commisions<br>
      or closing costs.Close quick. No hassles with solutions<br>
      to meet your unique situation.<br>
      Call today for an offer within 24 hours.
    </p>
  </section>

  <section class="card card-front" aria-label="Card front">
    <div class="brand">
      <span class="brand-mark" aria-hidden="true"></span>
      <span class="brand-name">KRV Home Solutions</span>
    </div>

    <ul class="contacts">
      <li>
        <svg class="icon" viewBox="0 0 24 24" aria-hidden="true"><circle cx="12" cy="12" r="12" fill="#1e3676"/><path d="M9 6.5c.5 0 1 .4 1.2.9l.6 1.8c.1.4 0 .8-.3 1.1l-.9.8c.6 1.3 1.7 2.4 3 3l.8-.9c.3-.3.7-.4 1.1-.3l1.8.6c.5.2.9.7.9 1.2v1.3c0 .7-.6 1.3-1.3 1.3C10.5 17.3 6.7 13.5 6.7 8.8c0-.7.6-1.3 1.3-1.3z" fill="#fff"/></svg>
        <span>555-014-2739</span>
      </li>
      <li><span class="dot" aria-hidden="true"></span><span>/krvhomesolutions</span></li>
      <li><span class="dot" aria-hidden="true"></span><span>@krvhomesolutions</span></li>
      <li>
        <svg class="icon" viewBox="0 0 24 24" aria-hidden="true"><circle cx="12" cy="12" r="12" fill="#1e3676"/><rect x="6" y="8" width="12" height="8.5" rx="1" fill="none" stroke="#fff" stroke-width="1.5"/><path d="M6.5 8.7 12 13l5.5-4.3" fill="none" stroke="#fff" stroke-width="1.5"/></svg>
        <span>KRVHOMESOLUTIONS@mailnest.example</span>
      </li>
    </ul>

    <div class="title-block">
      <h1 class="company">KRV HOME SOLUTIONS</h1>
      <p class="role">Principal-Acquisitions</p>
    </div>
    <span class="edge-bar" aria-hidden="true"></span>

    <p class="slogan">Selling a home fast</p>
  </section>

</main>
</body>
</html>
```